Small holiday retreat needs new Internet launch

"The Evolution from a Ruin into a Holiday Retreat.
My wife and I rebuilt a small farm in a remote village into a little holiday retreat. Though close to the Baltic Sea, we want to attract people with the desire to spend some days in a secluded place. Though remote it offers some luxury - and time ticks slower.
This summer was our third season and we want to adapt our Internet pages. Look at our business card - we want to keep this style.
It should be a bit mystic and should not attract the bargain hunter.
We realized that in summer our name "Wiesenkrone" (ie sunny hill) does not fit for the dark part of the year - then it is more like "Glimmering Moors".
We have a guesthouse (the former stable) and two tiny houses. Additionally, we have lavatory with sauna in the rebuilt barn and a fitness room.
On our farm live a few animals (dog, cats, chicken, bees) + wild visitors.
Our current home page is www.wiesenkrone-example.net
A few pictures are on Mapvista Atlas and I can share more in Cloudkeep Vault.
The final homepage should also offer translations into English, French, Dutch.
Better and consistent fonts.
No "galery" but more "four seasons".

Target Market(s)

Individual travellers - not just from Germany!

Industry/Entity Type

Tourism

Coding

Coded - Design and coding required

Number of Pages Required

4 page

Font styles to use
Script

Colors
FFC000
F8CF3A
FAE287
FDF2CF
FEFAEE

Requirements
Must have
• A "mystic" and romantic appearance.
Nice to have
• See my comments.

```html
<!DOCTYPE html>
<html lang="en">
<head>
<meta charset="utf-8">
<title>Wiesenkrone – Holiday Retreat</title>
<link href="https://fonts.googleapis.com/css2?family=Cormorant+Garamond:wght@400;500&family=Great+Vibes&family=Jost:wght@400;500;600&display=swap" rel="stylesheet">
<style>
:root{
  --gold:#F0B126;
  --gold-light:#F8CF3A;
  --gold-pale:#FAE287;
  --cream:#FEFAEE;
  --dark:#3A2C12;
  --ink:#2b2b2b;
  --muted:#555;
  --green:#2f5b3a;
}
*{margin:0;padding:0;box-sizing:border-box}
html,body{width:1200px;height:4392px;overflow:hidden}
body{position:relative;background:#fff;font-family:"Jost",sans-serif;color:var(--ink)}
.abs{position:absolute}
.serif{font-family:"Cormorant Garamond",serif;font-weight:500;letter-spacing:1px}
.script{font-family:"Great Vibes",cursive;font-weight:400}
.btn{position:absolute;display:flex;align-items:center;justify-content:center;border-radius:24px;background:var(--gold);color:#fff;font-weight:600;font-size:14px;letter-spacing:1px;text-transform:uppercase}
.photo{position:absolute}

/* header */
.header{position:absolute;left:0;top:0;width:1200px;height:75px;background:#fff;z-index:5}
.logo{position:absolute;left:106px;top:18px;display:flex;align-items:center;gap:10px;color:var(--gold);font-size:26px;font-weight:500}
.logo .dot{width:34px;height:34px;border-radius:50%;background:var(--gold-light)}
.nav a{position:absolute;top:29px;font-size:12px;font-weight:600;letter-spacing:.6px;color:#222;text-decoration:none;text-transform:uppercase}
.nav .active::after{content:"";position:absolute;left:0;right:0;top:39px;height:3px;background:var(--gold)}
.nav .contact{top:22px;left:934px;width:101px;height:31px;background:#C99A1E;color:#fff;display:flex;align-items:center;justify-content:center;font-size:11px}
.lang{position:absolute;left:1060px;top:27px;display:flex;gap:6px;align-items:center}
.lang .flag{width:22px;height:22px;border-radius:50%;background:#2d3e8c;border:2px solid #c8102e}

/* hero */
.hero{left:0;top:75px;width:1200px;height:633px;background:linear-gradient(180deg,#1b56c9 0%,#4f8fe3 35%,#9cc3ea 52%,#4d7a34 62%,#3f7d2a 100%)}
.hero-title{left:124px;top:248px;color:#fff}
.hero-title .script{font-size:72px;line-height:1}
.hero-title .serif{font-size:52px;line-height:1;margin-top:4px;letter-spacing:2px;font-weight:400}
.booking{left:745px;top:200px;width:353px;height:351px;background:#D9A52A}
.field{position:absolute;left:27px;width:300px;height:41px;border-radius:21px;background:#fff;display:flex;align-items:center;padding-left:20px;gap:10px;font-size:13px;color:#555}
.field svg{flex:none}
.booking .book{left:32px;top:272px;width:296px;height:46px;background:var(--dark);font-size:15px}

/* welcome */
.rounded{border-radius:24px}
.welcome-script{left:653px;top:800px;font-size:78px;color:var(--gold);line-height:1}
.h2{position:absolute;font-family:"Cormorant Garamond",serif;font-weight:400;font-size:36px;line-height:42px;color:#222;letter-spacing:1px;text-transform:uppercase}
.rule{position:absolute;height:2px;width:72px;background:var(--green)}
.para{position:absolute;font-size:14px;line-height:25px;color:#444}

/* seasons */
.section-title{position:absolute;left:0;width:1200px;text-align:center;font-family:"Cormorant Garamond",serif;font-size:36px;color:#222;letter-spacing:1px}
.season{position:absolute;top:1628px;width:244px;height:295px;background:#fff;box-shadow:0 4px 10px rgba(0,0,0,.12)}
.season .photo{left:0;top:0;width:244px;height:250px}
.season .label{position:absolute;left:0;bottom:14px;width:100%;text-align:center;font-size:16px;font-weight:600;letter-spacing:.5px;color:#222;text-transform:uppercase}
.season.featured{top:1608px;height:329px;background:var(--dark)}
.season.featured .label{color:#fff;bottom:auto;top:236px}
.season.featured .sub{position:absolute;left:20px;right:20px;top:264px;text-align:center;color:#eee;font-size:11.5px;line-height:16px}

/* resources */
.res{position:absolute;top:2210px;height:310px}
.res .name{position:absolute;left:0;width:100%;text-align:center;color:#fff;font-size:22px;font-weight:600;letter-spacing:1px;text-transform:uppercase}
.res .under{position:absolute;height:2px;width:46px;background:#fff}

/* contact */
.contact-item{position:absolute;left:133px;display:flex;gap:20px;align-items:flex-start}
.contact-item .ic{width:42px;height:42px;border-radius:50%;background:var(--gold);display:flex;align-items:center;justify-content:center;flex:none;margin-top:2px}
.contact-item small{display:block;font-size:15px;color:#444}
.contact-item b{display:block;font-size:21px;font-weight:400;color:#222;line-height:26px}
.form-panel{left:595px;top:3338px;width:488px;height:392px;background:var(--gold);border-radius:60px 0 60px 0}
.input{position:absolute;left:48px;width:400px;height:42px;border:1.5px solid #fff;display:flex;align-items:center;gap:10px;padding-left:14px;font-size:13px;color:#fff}
.send{position:absolute;left:48px;top:311px;width:170px;height:44px;background:var(--dark);color:#fff;font-size:13px;font-weight:600;display:flex;align-items:center;justify-content:center;letter-spacing:.5px}

/* footer */
.footer{left:0;top:3990px;width:1200px;height:402px;background:var(--dark)}
.fcol{position:absolute;top:4060px;border-left:3px solid #fff;padding-left:14px}
.fcol h4{font-family:"Jost",sans-serif;font-size:19px;font-weight:500;color:#fff;letter-spacing:.5px}
.flinks{position:absolute;color:#e6e0d2;font-size:13px;line-height:33px}
.finfo{position:absolute;left:494px;display:flex;gap:12px;align-items:flex-start;color:#e6e0d2;font-size:12px;line-height:20px}
.finfo .ic{width:24px;height:24px;border-radius:50%;background:#fff;flex:none;display:flex;align-items:center;justify-content:center}
.social{position:absolute;top:4212px;width:26px;height:26px;border-radius:50%;border:2px solid var(--gold);background:#fff}
</style>
</head>
<body>

<!-- header -->
<header class="header">
  <div class="logo"><span class="dot"></span>Wiesenkrone</div>
  <nav class="nav">
    <a class="active" style="left:375px">Über uns</a>
    <a style="left:494px">Unterkünfte</a>
    <a style="left:639px">Buchungen &amp; Kalender</a>
    <a style="left:839px">Galerie</a>
    <a class="contact">Kontakt</a>
  </nav>
  <div class="lang"><span class="flag"></span>
    <svg width="12" height="8" viewBox="0 0 12 8"><path d="M1 1l5 5 5-5" stroke="#333" stroke-width="1.5" fill="none"/></svg></div>
</header>

<!-- hero -->
<div class="abs hero" role="img" aria-label="Photo of a tiny house wagon on a green meadow under a bright blue sky"></div>
<div class="abs hero-title">
  <div class="script">Reise in Deine</div>
  <div class="serif">ENTSPANNUNG</div>
</div>
<div class="btn" style="left:126px;top:400px;width:181px;height:45px">Book Retreat</div>

<div class="abs booking">
  <div class="field" style="top:40px"><svg width="16" height="16" viewBox="0 0 16 16"><rect x="1.5" y="3" width="13" height="11.5" rx="1.5" fill="none" stroke="#555"/><path d="M1.5 6.5h13M5 1.5v3M11 1.5v3" stroke="#555"/></svg>Arrival Date</div>
  <div class="field" style="top:98px"><svg width="16" height="16" viewBox="0 0 16 16"><rect x="1.5" y="3" width="13" height="11.5" rx="1.5" fill="none" stroke="#555"/><path d="M1.5 6.5h13M5 1.5v3M11 1.5v3" stroke="#555"/></svg>Departure Date</div>
  <div class="field" style="top:156px"><svg width="16" height="18" viewBox="0 0 16 18"><circle cx="8" cy="3" r="2.5" fill="#444"/><path d="M4 7h8v5h-2v6H6v-6H4z" fill="#444"/></svg>Adults</div>
  <div class="field" style="top:214px"><svg width="16" height="18" viewBox="0 0 16 18"><circle cx="8" cy="3" r="2.5" fill="none" stroke="#444"/><path d="M5 7h6l2 6H3z M6 13v5M10 13v5" fill="none" stroke="#444"/></svg>Childrens</div>
  <div class="btn book">Book Now</div>
</div>

<svg class="abs" style="left:0;top:590px" width="1200" height="120" viewBox="0 0 1200 120">
  <path d="M0 95 L40 88 60 100 110 90 150 104 190 92 230 96 270 84 300 72 330 58 360 50 400 70 420 64 450 78 470 60 500 40 540 28 560 40 590 30 620 52 650 40 680 62 700 48 740 66 780 54 820 70 860 58 900 76 940 68 980 84 1020 70 1060 86 1100 74 1140 90 1170 82 1200 96 L1200 120 L0 120 Z" fill="#fff"/>
</svg>

<!-- welcome -->
<div class="photo rounded" style="left:136px;top:820px;width:208px;height:183px;background:linear-gradient(135deg,#8a4a2c,#c07a45 55%,#5a3a28)" role="img" aria-label="Portrait of the host at a table"></div>
<div class="photo rounded" style="left:356px;top:795px;width:241px;height:213px;background:linear-gradient(135deg,#d8d2c8,#8a8176 60%,#5f6670)" role="img" aria-label="Bedroom under a wooden roof"></div>
<div class="photo rounded" style="left:106px;top:1016px;width:240px;height:212px;background:linear-gradient(160deg,#3f6a2c,#8b8f8a 55%,#5b4a3a)" role="img" aria-label="Garden lounge sofa with breakfast table"></div>
<div class="photo rounded" style="left:360px;top:1020px;width:204px;height:184px;background:linear-gradient(180deg,#3e7ad8 0%,#8fb8e8 45%,#6aa04a 60%,#4f7d34)" role="img" aria-label="Tiny house on a meadow"></div>

<div class="abs script welcome-script">Welcome</div>
<div class="h2" style="left:663px;top:880px">Wiesenkrone in<br>beautifulCarinerland</div>
<div class="rule" style="left:663px;top:965px"></div>
<p class="para" style="left:665px;top:987px;width:466px">Welcome to the Wiesenkrone in beautiful Carinerland. With great attention to detail, we have turned our old farm into a place of rest and relaxation. Whether in the tiny house "Amber" or the holiday apartments "Westwind" and "Ostwind", in all of our accommodations we attach great importance to the fact that you as a guest immediately feel</p>
<div class="btn" style="left:661px;top:1141px;width:179px;height:44px">Learn More</div>

<!-- seasons band -->
<svg class="abs" style="left:0;top:1290px" width="1200" height="770" viewBox="0 0 1200 770">
  <defs><linearGradient id="band" x1="0" y1="0" x2="0" y2="1"><stop offset="0" stop-color="#F8CF3A"/><stop offset="1" stop-color="#F1AE1C"/></linearGradient></defs>
  <path d="M0 24 C300 90 700 110 1200 20 L1200 660 C900 720 500 640 200 690 C110 704 40 720 0 752 Z" fill="url(#band)"/>
  <path d="M0 10 C260 76 640 100 1200 14" fill="none" stroke="#F0B126" stroke-width="5"/>
  <path d="M0 24 C300 90 700 110 1200 20" fill="none" stroke="#fff" stroke-width="2"/>
</svg>
<div class="section-title" style="top:1438px">OUR SEASONS</div>
<div class="rule" style="left:572px;top:1490px;width:56px;background:#5a4a20"></div>
<p class="abs" style="left:140px;top:1515px;width:920px;text-align:center;font-size:17px;line-height:23px;color:#333">In a quiet and idyllic location, you can still quickly reach the Hanseatic cities of Wismar and Rostock as well as the beaches of Kuehlungsborn, Salzhaff and Rerik. We look forward to your visit.</p>

<div class="season" style="left:107px">
  <div class="photo" style="background:linear-gradient(180deg,#5b8fd6,#9cb8d6 35%,#c98a3a 60%,#4d7a2f)" role="img" aria-label="Farmhouse in summer"></div>
  <svg class="abs" style="left:0;top:200px" width="244" height="52" viewBox="0 0 244 52"><path d="M0 30 C60 0 120 50 244 18 L244 52 L0 52Z" fill="#fff"/><path d="M0 30 C60 0 120 50 244 18" stroke="#F0B126" stroke-width="4" fill="none"/></svg>
  <div class="label">Summer Season</div>
</div>
<div class="season featured" style="left:360px">
  <div class="photo" style="height:200px;background:linear-gradient(180deg,#4a4a48,#9a9a98 45%,#e6e6e4 70%,#6a6a68)" role="img" aria-label="Snow-covered sauna hut in winter"></div>
  <svg class="abs" style="left:0;top:168px" width="244" height="40" viewBox="0 0 244 40"><path d="M0 26 C60 0 130 40 244 12 L244 40 L0 40Z" fill="#3A2C12"/><path d="M0 26 C60 0 130 40 244 12" stroke="#F0B126" stroke-width="4" fill="none"/></svg>
  <div class="label">Winter Season</div>
  <div class="sub">Lorem ipsum dolor sit amet, consectetur adipiscing eli sed</div>
</div>
<div class="season" style="left:614px">
  <div class="photo" style="background:linear-gradient(135deg,#7a3b1c,#c56b2c 50%,#e3a35a)" role="img" aria-label="Cosy room with a wood stove"></div>
  <svg class="abs" style="left:0;top:200px" width="245" height="52" viewBox="0 0 245 52"><path d="M0 30 C60 0 120 50 245 18 L245 52 L0 52Z" fill="#fff"/><path d="M0 30 C60 0 120 50 245 18" stroke="#F0B126" stroke-width="4" fill="none"/></svg>
  <div class="label">Spring Season</div>
</div>
<div class="season" style="left:873px">
  <div class="photo" style="background:linear-gradient(180deg,#b8c8d8,#d9a050 50%,#5a7a3a 75%,#b84a3a)" role="img" aria-label="Farmhouse with flower garden"></div>
  <svg class="abs" style="left:0;top:200px" width="244" height="52" viewBox="0 0 244 52"><path d="M0 30 C60 0 120 50 244 18 L244 52 L0 52Z" fill="#fff"/><path d="M0 30 C60 0 120 50 244 18" stroke="#F0B126" stroke-width="4" fill="none"/></svg>
  <div class="label">Rainy Season</div>
</div>

<!-- resources -->
<div class="section-title" style="top:2106px">OUR RESOURCES</div>
<div class="rule" style="left:562px;top:2155px;width:76px;background:#5a4a20"></div>

<div class="res" style="left:104px;width:327px;background:linear-gradient(135deg,#6a3a22,#a86a3a 45%,#4a3a30)" role="img" aria-label="Rustic kitchen with exposed brick and beams">
  <div class="name" style="top:256px">Our Activites</div>
  <div class="under" style="left:140px;top:290px"></div>
</div>
<div class="res" style="left:789px;width:328px;background:linear-gradient(180deg,#7a6a9a,#c99aa8 35%,#4a6a3a 60%,#3a5a2a)" role="img" aria-label="Meadow with boulders at dusk">
  <div class="name" style="top:248px">Our Gallery</div>
  <div class="under" style="left:141px;top:282px"></div>
</div>
<div class="res" style="left:431px;top:2189px;width:358px;height:346px;background:linear-gradient(180deg,#2f3f58,#44556a 50%,#3c5538)" role="img" aria-label="Tiny house wagon in the evening">
  <div class="abs" style="left:8px;top:8px;right:8px;bottom:8px;border:1.5px solid #fff"></div>
  <div class="name" style="top:110px">Booking Calendar</div>
  <p class="abs" style="left:40px;width:278px;top:150px;text-align:center;color:#fff;font-size:14px;line-height:17px">Lorem ipsum dolor sit amet, consectetur adipiscing eli sed Lorem ipsum</p>
  <div class="btn" style="left:102px;top:212px;width:178px;height:44px;font-size:14px">Book Now</div>
</div>

<!-- feature block -->
<div class="abs" style="left:495px;top:2634px;width:705px;height:544px;background:var(--gold)"></div>
<svg class="abs" style="left:0;top:2609px" width="620" height="592" viewBox="0 0 620 592">
  <defs><linearGradient id="wagon" x1="0" y1="0" x2="0" y2="1"><stop offset="0" stop-color="#d88a5a"/><stop offset=".35" stop-color="#8fa0b8"/><stop offset=".7" stop-color="#4a7a30"/><stop offset="1" stop-color="#3a6a28"/></linearGradient></defs>
  <path d="M0 0 L470 0 C580 80 640 260 590 400 C560 490 520 560 480 592 L0 592Z" fill="url(#wagon)" role="img" aria-label="Blue shepherd's wagon with wooden stairs at sunset"/>
  <path d="M470 0 C580 80 640 260 590 400 C560 490 520 560 480 592" fill="none" stroke="#fff" stroke-width="8"/>
</svg>
<div class="h2" style="left:664px;top:2756px">Wiesenkrone in<br>beautifulCarinerland</div>
<div class="rule" style="left:672px;top:2846px;background:#fff;width:70px"></div>
<p class="para" style="left:667px;top:2874px;width:470px;color:#2b2b2b">Welcome to the Wiesenkrone in beautiful Carinerland. With great attention to detail, we have turned our old farm into a place of rest and relaxation. Whether in the tiny house "Amber" or the holiday apartments "Westwind" and "Ostwind", in all of our accommodations we attach great importance to the fact that you as a guest immediately feel</p>
<div class="btn" style="left:670px;top:3023px;width:225px;height:51px;background:#D9A52A;border-radius:26px">Explore Packages</div>

<!-- contact -->
<div class="abs" style="left:0;top:3200px;width:1200px;height:560px;background:linear-gradient(180deg,#f6f5f2,#eeece6)"></div>
<div class="h2" style="left:123px;top:3350px;font-size:38px">Contact Us</div>
<div class="rule" style="left:389px;top:3370px;width:72px"></div>
<p class="para" style="left:124px;top:3425px;width:390px;font-size:15px;line-height:24px">Lorem Ipsum is simply dummy text of the printing and typesetting industry Lorem Ipsum.</p>

<div class="contact-item" style="top:3515px"><span class="ic"><svg width="20" height="20" viewBox="0 0 24 24"><path d="M6.6 10.8a15 15 0 006.6 6.6l2.2-2.2a1 1 0 011-.25 11.4 11.4 0 003.6.57 1 1 0 011 1V20a1 1 0 01-1 1A17 17 0 013 4a1 1 0 011-1h3.5a1 1 0 011 1c0 1.25.2 2.45.57 3.6a1 1 0 01-.25 1z" fill="#fff"/></svg></span>
  <div><small>Phone Number</small><b style="font-weight:500">+49 157 000 414 26</b></div></div>
<div class="contact-item" style="top:3585px"><span class="ic"><svg width="20" height="16" viewBox="0 0 20 16"><rect x="1" y="1" width="18" height="14" rx="2" fill="none" stroke="#fff" stroke-width="2"/><path d="M1 2l9 7 9-7" fill="none" stroke="#fff" stroke-width="2"/></svg></span>
  <div><small>Write Email us</small><b>hallo@wiesenkrone-example.de</b></div></div>
<div class="contact-item" style="top:3665px"><span class="ic"><svg width="18" height="22" viewBox="0 0 18 22"><path d="M9 1a8 8 0 00-8 8c0 6 8 12 8 12s8-6 8-12a8 8 0 00-8-8z" fill="#fff"/><circle cx="9" cy="9" r="3" fill="#F0B126"/></svg></span>
  <div><small>Address</small><b>Lindenweg 9, 18299<br>Feldhausen, Germany</b></div></div>

<div class="abs form-panel">
  <div class="input" style="top:52px"><svg width="14" height="14" viewBox="0 0 14 14"><circle cx="7" cy="4" r="3" fill="#fff"/><path d="M1 14c0-4 3-5 6-5s6 1 6 5z" fill="#fff"/></svg>First name</div>
  <div class="input" style="top:106px"><svg width="14" height="14" viewBox="0 0 24 24"><path d="M6.6 10.8a15 15 0 006.6 6.6l2.2-2.2a1 1 0 011-.25 11.4 11.4 0 003.6.57 1 1 0 011 1V20a1 1 0 01-1 1A17 17 0 013 4a1 1 0 011-1h3.5a1 1 0 011 1c0 1.25.2 2.45.57 3.6a1 1 0 01-.25 1z" fill="#fff"/></svg>Phone number</div>
  <div class="input" style="top:161px"><svg width="14" height="11" viewBox="0 0 20 16"><rect x="1" y="1" width="18" height="14" fill="none" stroke="#fff" stroke-width="2"/><path d="M1 2l9 7 9-7" fill="none" stroke="#fff" stroke-width="2"/></svg>Email address</div>
  <div class="input" style="top:213px;height:81px;align-items:flex-start;padding-top:12px">Comments</div>
  <div class="send">SEND MESSAGE</div>
</div>

<!-- landscape strip -->
<div class="abs" style="left:0;top:3740px;width:1200px;height:270px;background:linear-gradient(180deg,#eeece6 0%,#7f9a6a 30%,#3f6a2c 60%,#5d8f3a 100%)" role="img" aria-label="Panorama of the farm meadow and trees"></div>

<!-- footer -->
<div class="abs footer"></div>
<svg class="abs" style="left:0;top:3950px" width="1200" height="80" viewBox="0 0 1200 80">
  <path d="M0 40 C300 -10 700 20 1200 2 L1200 80 L0 80Z" fill="#F0B126"/>
  <path d="M0 56 C320 6 720 34 1200 14 L1200 80 L0 80Z" fill="#3A2C12"/>
</svg>

<div class="fcol" style="left:136px;height:150px"><h4>Quick Links</h4></div>
<div class="flinks" style="left:155px;top:4100px">About<br>Accommodation<br>Booking Calendar</div>
<div class="flinks" style="left:312px;top:4100px">Our Gallery<br>Sitemap<br>Contact</div>

<div class="fcol" style="left:467px;height:150px"><h4>Contact Us</h4></div>
<div class="finfo" style="top:4102px"><span class="ic"><svg width="10" height="13" viewBox="0 0 18 22"><path d="M9 1a8 8 0 00-8 8c0 6 8 12 8 12s8-6 8-12a8 8 0 00-8-8z" fill="#3A2C12"/></svg></span><span>Lindenweg 9, 18299<br>Feldhausen, Germany</span></div>
<div class="finfo" style="top:4156px"><span class="ic"><svg width="12" height="9" viewBox="0 0 20 16"><rect x="1" y="1" width="18" height="14" fill="none" stroke="#3A2C12" stroke-width="2"/><path d="M1 2l9 7 9-7" fill="none" stroke="#3A2C12" stroke-width="2"/></svg></span><span style="line-height:24px">hallo@wiesenkrone-example.de</span></div>
<div class="finfo" style="top:4190px"><span class="ic"><svg width="11" height="11" viewBox="0 0 24 24"><path d="M6.6 10.8a15 15 0 006.6 6.6l2.2-2.2a1 1 0 011-.25 11.4 11.4 0 003.6.57 1 1 0 011 1V20a1 1 0 01-1 1A17 17 0 013 4a1 1 0 011-1h3.5a1 1 0 011 1c0 1.25.2 2.45.57 3.6a1 1 0 01-.25 1z" fill="#3A2C12"/></svg></span><span style="line-height:24px">+49 157 000 414 26</span></div>

<div class="fcol" style="left:769px;height:40px"><h4>Sign Up Newsletter</h4></div>
<div class="abs" style="left:794px;top:4109px;width:256px;height:37px;background:#fff;font-size:11px;color:#444;padding:12px 18px">Email address</div>
<div class="abs" style="left:794px;top:4158px;width:256px;height:38px;background:var(--gold);color:#fff;font-size:12px;font-weight:600;display:flex;align-items:center;justify-content:center;letter-spacing:.5px">SUBSCRIBE</div>
<span class="social" style="left:794px"></span>
<span class="social" style="left:833px"></span>
<span class="social" style="left:871px"></span>
<span class="social" style="left:910px"></span>

<div class="abs" style="left:108px;top:4330px;width:978px;height:1px;background:#8a7a58"></div>
<div class="abs" style="left:0;top:4348px;width:1200px;text-align:center;color:#e6e0d2;font-size:12px">Copyright: 2020 Wiesenkrone &nbsp;|&nbsp; Privacy Policy | Terms of Use</div>

</body>
</html>
```